Medical Learning Web Design Project

The web site will be a site for medical students. It is aimed at providing a collaborative place for students to study, learn, question each other and challenge each other with learning. The site needs to have a section on the page that is for the content and this needs to be relatively clean and clinical. The surrounding elements will be informative (for the statistics, challenge etc). There will also be a slide-out screen that allows for the social/friend elements of the site.

The colour scheme needs to be clean and clinical where appropriate, but also engaging and exciting for the social/competitive elements.
Updates

Just for clarity: The site isn't expected to be 'coded' ... it is just the layered PSD files that I need.

Also, with regards to the navigation buttons ... they will never ALL be present at the same time so don't feel the need to design all on one page, but creativity around allowing few or many on a page will be an advantage ...

Thanks

Hi,

Please note that the image uploaded has been done as a wireframe by the developers. I am looking for a more creative and engaging way of presenting that content ...

Thanks

Hi all

Thank you all for the designs so far ...!

Please have a look at the new uploaded file, I am also looking not just for a 'templated home page' but also some different layouts that are represented in these wireframes. If the various layouts represented can be condensed down into 1 or 2 page templates with appropriate colour schemes to capture the type of content on the page (as already mentioned ... social .. competitive ... learning), then that will help me live the concepts better too! The friends tab for instance I have envisaged as a slider covering the screen and then sliding back when complete ... but let me see what creativity you can give to this ...!

Many thanks

Target Market(s)

Medical Students

Industry/Entity Type

Medical

Requirements
Must have
• - Not cluttered appearance
- Dynamic navigation (ie. site will be developed to only show relevant navigation buttons on each page ...)
- Navigation buttons (need to be individual buttons) will be: 'Home', 'Take the tour', 'What your peers say', 'Subscriptions', 'Free Signup', 'Contact us', 'Moderation', 'Statistics', 'Competition', 'Answer Questions', 'Post Questions', 'My profile', 'Friends'
- Please also ensure it is engaging for social elements and competitive elements (perhaps slightly different design for pages focussed on each element)
- Please also ensure that there is a masculine design and feminine design that has continuity for the site but depending on gender the design can be tailored to be more appealing (that means perhaps male social design, male competitive design, female social design, female competitive design ... without loosing continuity through the site).
- Photoshop PSD format
- Pixel perfect at least 1000 pixels wide (but the design needs to allow for various monitor sizes (only desktop or laptops ... not tablets or smart phones)

```html
<!DOCTYPE html>
<html lang="en">
<head>
<meta charset="utf-8">
<title>Clinova – The Medical Peer Review</title>
<link href="https://fonts.googleapis.com/css2?family=Arimo:wght@400;700&display=swap" rel="stylesheet">
<style>
  :root{
    --brand-blue:#2a6891;
    --brand-blue-dark:#1f5479;
    --sky:#cfe0ee;
    --sky-soft:#e6f0f7;
    --page-grey:#f1f1f1;
    --white:#ffffff;
    --ink:#1a1a1a;
    --nav-ink:#3a3a3a;
    --muted:#8a8a8a;
    --link-blue:#1b6db3;
    --accent-green:#3fa535;
    --video-black:#1c1c1c;
    --social-a:#2d5aa8;
    --social-b:#2fa8e0;
    --social-c:#f08a1c;
  }
  *{margin:0;padding:0;box-sizing:border-box}
  html,body{width:1200px;height:841px;overflow:hidden;background:var(--white)}
  body{font-family:"Arimo",Arial,sans-serif;color:var(--ink);position:relative}
  .abs{position:absolute}

  .top-band{left:83px;top:0;width:1117px;height:235px;
    background:radial-gradient(ellipse 70% 120% at 50% 100%, #3d7aa3 0%, var(--brand-blue) 55%, #245e85 100%);}
  .grey-field{left:83px;top:235px;width:1117px;height:561px;background:var(--page-grey)}
  .footer-band{left:83px;top:796px;width:1117px;height:45px;background:var(--brand-blue)}
  .page{left:291px;top:2px;width:690px;height:794px;background:var(--white)}
  .page-foot-line{left:291px;top:790px;width:690px;height:6px;background:var(--sky-soft)}

  .logo{left:323px;top:14px}
  .logo-name{font-size:32px;font-weight:400;color:var(--brand-blue);letter-spacing:-0.5px;line-height:1}
  .logo-tag{font-size:5.5px;font-weight:700;color:var(--nav-ink);letter-spacing:0.3px;margin-top:3px}

  .signin{left:606px;top:16px;width:114px;height:17px;background:var(--sky-soft)}
  .signin-btn{width:42px;height:17px;background:var(--brand-blue-dark);color:var(--white);font-size:6.5px;font-weight:700;display:flex;align-items:center;justify-content:center}
  .account-links{left:734px;top:20px;font-size:7.5px;color:var(--nav-ink)}
  .account-links span{margin-right:9px}
  .social{display:flex;gap:5px}
  .social i{display:block;width:14px;height:14px;border-radius:2px}
  .social i:nth-child(1){background:var(--social-a)}
  .social i:nth-child(2){background:var(--social-b)}
  .social i:nth-child(3){background:var(--social-c)}
  .social-top{left:828px;top:16px}

  .nav{left:381px;top:79px;height:22px;display:flex;font-size:8.4px;font-weight:700;color:var(--nav-ink)}
  .nav a{color:inherit;text-decoration:none;display:flex;align-items:center;padding:0 9px;height:22px;letter-spacing:0.1px}
  .nav a.active{background:var(--sky);padding:0 12px}
  .nav-strip{left:322px;top:101px;width:631px;height:5px;background:var(--sky)}

  .hero{left:322px;top:106px;width:631px;height:214px;background:var(--sky)}
  .hero-photo{left:322px;top:106px;width:310px;height:210px;
    background:linear-gradient(100deg,#a9c6e0 0%,#dfe9f3 35%,#c7d9ea 70%,#8fb1cf 100%)}
  .hero-panel{left:322px;top:106px}
  .hero-title{left:654px;top:118px;color:var(--white);font-size:24px;font-weight:700;line-height:1}
  .hero-sub{left:654px;top:145px;color:var(--white);font-size:16.5px}
  .hero-list{left:683px;top:173px;list-style:none;color:var(--white);font-size:9.2px}
  .hero-list li{height:15.8px;position:relative;padding-left:14px}
  .hero-list li::before{content:"";position:absolute;left:0;top:1px;width:8px;height:8px;border-radius:50%;background:var(--accent-green)}

  .dots{left:595px;top:330px;display:flex;gap:8px}
  .dots i{width:9px;height:9px;border-radius:50%;background:#b8b8b8}
  .dots i:first-child{background:var(--sky)}

  .video{left:329px;top:363px;width:262px;height:196px;background:var(--video-black)}
  .video-still{left:337px;top:370px;width:246px;height:182px;
    background:linear-gradient(180deg,#d4e1ec 0%,#b5c9da 60%,#8e9aa6 100%)}
  .video-controls{left:329px;top:564px;width:262px;height:27px;background:var(--video-black)}

  .works-title{left:617px;top:360px;font-size:22px;font-weight:400;color:var(--brand-blue)}
  .works-lead{left:617px;top:395px;font-size:14px;font-weight:400;color:var(--muted)}
  .works-body{left:617px;top:422px;width:322px;font-size:8.8px;line-height:10.8px;color:var(--ink)}
  .works-body p{margin-bottom:10.8px}

  .feature{top:626px;width:145px}
  .feature-icon{display:block;width:56px;height:56px;margin-left:32px;border-radius:4px}
  .feature h3{margin-top:17px;font-size:10.2px;font-weight:700;color:var(--link-blue)}
  .feature p{margin-top:12px;font-size:7.5px;line-height:9.5px;color:var(--ink)}

  .foot-logo{left:330px;top:802px}
  .foot-logo .logo-name{font-size:22px;color:var(--white)}
  .foot-logo .logo-tag{font-size:4px;color:var(--white);margin-top:1px}
  .foot-links{top:813px;font-size:7.5px;font-weight:700;color:var(--white)}
  .social-foot{left:892px;top:809px}
  .social-foot i{width:17px;height:17px}
</style>
</head>
<body>
  <div class="abs top-band"></div>
  <div class="abs grey-field"></div>
  <div class="abs footer-band"></div>
  <div class="abs page"></div>
  <div class="abs page-foot-line"></div>

  <header>
    <div class="abs logo">
      <div class="logo-name">Clinova</div>
      <div class="logo-tag">THE MEDICAL PEER REVIEW</div>
    </div>
    <div class="abs signin"><div class="signin-btn">SIGN IN</div></div>
    <div class="abs account-links"><span>Sign up</span><span>My Account</span></div>
    <div class="abs social social-top"><i></i><i></i><i></i></div>

    <nav class="abs nav">
      <a class="active" href="#">HOME</a>
      <a href="#">TAKE THE TOUR</a>
      <a href="#">WHAT YOUR PEERS SAY</a>
      <a href="#">SUBSCRIPTION PLANS</a>
      <a href="#">FREE SIGNUP</a>
      <a href="#">CONTACT US</a>
    </nav>
    <div class="abs nav-strip"></div>
  </header>

  <section class="hero-slider">
    <div class="abs hero"></div>
    <svg class="abs hero-panel" width="631" height="210" viewBox="0 0 631 210">
      <rect x="0" y="0" width="631" height="210" fill="var(--brand-blue)"/>
      <path d="M0 0 H340 C300 20 170 40 0 100 Z" fill="#6f9bc0"/>
      <path d="M310 210 C420 140 540 110 631 95 V210 Z" fill="#3a789f" opacity="0.7"/>
    </svg>
    <div class="abs hero-photo" role="img" aria-label="Group of smiling doctors and nurses in white coats and scrubs"></div>
    <div class="abs hero-title">Clinova</div>
    <div class="abs hero-sub">The Medical Peer Review.</div>
    <ul class="abs hero-list">
      <li>Test your medical knowledge.</li>
      <li>Anwer a vast most array of medical questions.</li>
      <li>Earn trophies as your knowledge increases.</li>
      <li>Rate questions from peers.</li>
      <li>Ask your own questions.</li>
      <li>Links to your friends and check their progress.</li>
      <li>29,903 Questions answered.</li>
    </ul>
    <div class="abs dots"><i></i><i></i><i></i><i></i><i></i></div>
  </section>

  <section class="how-it-works">
    <div class="abs video"></div>
    <div class="abs video-still" role="img" aria-label="Video still of a doctor standing in a bright hospital corridor with colleagues behind"></div>
    <svg class="abs" style="left:436px;top:441px" width="46" height="46" viewBox="0 0 46 46">
      <circle cx="23" cy="23" r="22" fill="#000" opacity="0.3"/>
      <path d="M17 12 L35 23 L17 34 Z" fill="#fff" opacity="0.6"/>
    </svg>
    <div class="abs video-controls"></div>
    <svg class="abs" style="left:329px;top:564px" width="262" height="27" viewBox="0 0 262 27">
      <rect x="8" y="8" width="2" height="11" fill="#bbb"/>
      <rect x="13" y="8" width="2" height="11" fill="#bbb"/>
      <path d="M24 7 L35 13.5 L24 20 Z" fill="#bbb"/>
      <rect x="43" y="12.5" width="210" height="2" fill="#777"/>
    </svg>

    <h1 class="abs works-title">How Clinova works</h1>
    <h2 class="abs works-lead">Lorem ipsum dolor sit amet.</h2>
    <div class="abs works-body">
      <p>consectetuer adipiscing elit, sed diam nonummy nibh euismod tincidunt ut laoreet dolore magna aliquam erat volutpat. Ut wisi enim ad minim veniam, quis nostrud exerci tation ullamcorper suscipit lobortis nisl ut aliquip ex ea commodo consequat.</p>
      <p>Duis autem vel eum iriure dolor in hendrerit in vulputate velit esse molestie consequat, vel illum dolore eu feugiat nulla facilisis at vero eros et accumsan et iusto odio dignissim qui blandit praesent luptatum zzril delenit augue duis dolore te feugait nulla facilisi.</p>
      <p>Nam liber tempor cum soluta nobis eleifend option congue nihil imperdiet doming id quod mazim placerat facer possim assum. Typi non habent claritatem insitam; est usus legentis in iis qui facit eorum claritatem. Investigationes demonstraverunt lectores legere me lius quod ii legunt saepius.</p>
    </div>
  </section>

  <section class="features">
    <div class="abs feature" style="left:330px">
      <div class="feature-icon" role="img" aria-label="Medical clipboard illustration" style="background:linear-gradient(135deg,#d9ead5,#c9d3dc)"></div>
      <h3>LOREM IPSUM DOLOR SIT</h3>
      <p>Duis autem vel eum iriure dolor in hendrerit in vulputate velit esse molestie consequat, vel illum dolore eu feugiat nulla facilisis at vero eros et accumsan et iusto odio dignissim</p>
    </div>
    <div class="abs feature" style="left:490px">
      <div class="feature-icon" role="img" aria-label="Medicine capsule and tablet illustration" style="background:linear-gradient(135deg,#d9ead5,#cdd9e8)"></div>
      <h3>CONSECTETUR ET</h3>
      <p>Vel illum dolore eu feugiat nulla facilisis at vero eros et accumsan et iusto odio dignissim.</p>
    </div>
    <div class="abs feature" style="left:651px">
      <div class="feature-icon" role="img" aria-label="X-ray viewer illustration" style="background:linear-gradient(135deg,#d5d8db,#c4c8cc)"></div>
      <h3>DOLOR SIT IPSUM</h3>
      <p>Duis autem vel eum iriure dolor in hendrerit in vulputate velit esse molestie consequat quid ipsum et dolore amet.</p>
    </div>
    <div class="abs feature" style="left:808px">
      <div class="feature-icon" role="img" aria-label="Heart monitor illustration" style="background:linear-gradient(135deg,#cfe0ee,#d9ead5)"></div>
      <h3>LOREM IPSUM DOLOR SIT</h3>
      <p>Duis autem vel eum iriure dolor in hendrerit in vulputate velit esse molestie consequat, vel illum dolore eu feugiat nulla facilisis at vero eros et accumsan et iusto odio dignissim</p>
    </div>
  </section>

  <footer>
    <div class="abs foot-logo">
      <div class="logo-name">Clinova</div>
      <div class="logo-tag">THE MEDICAL PEER REVIEW</div>
    </div>
    <div class="abs foot-links" style="left:466px">Privacy Policy &nbsp;&nbsp;|&nbsp;&nbsp; Sitemap</div>
    <div class="abs foot-links" style="left:640px">Copyright 2012</div>
    <div class="abs foot-links" style="left:792px">Sign up</div>
    <div class="abs foot-links" style="left:832px">Login</div>
    <div class="abs social social-foot"><i></i><i></i><i></i></div>
  </footer>
</body>
</html>
```